Retractable Banner Stands

Hello we need a deisgn for a banner.
Sizes: 36"x80", 12"x17"(this one to have less on it, most the logo, license numvber, and address), and a 24"x40" banner
Roofing Services
HOA & Commercial Roofing
• Emergency roof tarping & repairs — Starting at $550
• Small & large roof repairs
• Preventative roof maintenance
• Full roof replacement
Deck & Balcony Services
• Balcony & deck maintenance
SB-326 Repairs
• Deck resurfacing
• Small & large deck repairs
• Full deck reconstruction
Gutter Services
• Small & large gutter repairs
• Gutter cleaning & maintenance
• New gutter installation & replacement
License Information:
C-39 Roofing Contractor
General B Contractor
License #4529730
📍 Serving Orange County & Surrounding Areas
📍 Office Location:
41 Dunwick Street, Suite F
Target Market(s)
HOA & Commerical roofs
Industry/Entity Type
Roofing
Other font styles liked:
- Gotham
Look and feel

```html
<!DOCTYPE html>
<html lang="en">
<head>
<meta charset="utf-8">
<title>Crestline Roofing &amp; Waterproofing — Banner</title>
<link rel="stylesheet" href="https://fonts.googleapis.com/css2?family=Montserrat:wght@500;600;700;800&family=Signika:wght@400;500;600&display=swap">
<style>
  :root {
    --brand-blue: #2f6ee6;
    --heading-blue: #2c68de;
    --text-blue: #3a73e3;
    --ink: #1a1a1a;
    --paper: #ffffff;
  }
  * { margin: 0; padding: 0; box-sizing: border-box; }
  html, body { width: 720px; height: 1200px; overflow: hidden; background: var(--paper); }
  .banner {
    position: relative; width: 720px; height: 1200px; overflow: hidden;
    background: var(--paper);
    font-family: "Signika", "Trebuchet MS", sans-serif;
  }
  .banner__shapes { position: absolute; inset: 0; }
  .brand { position: absolute; top: 44px; left: 0; width: 746px; text-align: center; color: var(--paper); }
  .brand__name {
    font-family: "Montserrat", sans-serif; font-weight: 800;
    font-size: 66px; letter-spacing: 2px; line-height: 1;
  }
  .brand__tagline {
    margin-top: 26px;
    font-family: "Montserrat", sans-serif; font-weight: 500;
    font-size: 19px; letter-spacing: 1px;
  }
  .headline {
    position: absolute; left: 392px; width: 312px; top: 266px; text-align: center;
    font-family: "Montserrat", sans-serif; font-weight: 700;
    font-size: 29px; line-height: 37px; color: var(--heading-blue);
  }
  .services { position: absolute; left: 406px; top: 420px; width: 300px; color: var(--text-blue); }
  .services__title {
    font-family: "Montserrat", sans-serif; font-weight: 600;
    font-size: 22px; color: var(--heading-blue); margin-bottom: 18px;
  }
  .service-group { margin-bottom: 24px; }
  .service-group__title { font-weight: 600; font-size: 13.5px; letter-spacing: .2px; margin-bottom: 16px; }
  .service-group__list { list-style: none; font-size: 13px; line-height: 17.4px; }
  .service-group__list li { padding-left: 11px; position: relative; }
  .service-group__list li::before {
    content: ""; position: absolute; left: 1px; top: 7px;
    width: 5px; height: 5px; border-radius: 50%; background: var(--text-blue);
  }
  .service-group__list li.note { padding-left: 11px; }
  .service-group__list li.note::before { display: none; }
  .contact { position: absolute; left: 407px; top: 955px; color: var(--ink); }
  .contact__label { font-size: 16px; font-weight: 500; }
  .contact__row { display: flex; align-items: flex-start; gap: 21px; margin: 13px 0 14px; }
  .contact__icon { width: 28px; height: 24px; flex: none; }
  .contact__phone { font-size: 28px; font-weight: 600; line-height: 1; margin-top: 2px; }
  .contact__address { font-size: 16px; font-weight: 500; line-height: 22px; margin-top: 6px; }
  .license {
    position: absolute; right: 380px; top: 1072px; text-align: right;
    color: var(--paper); font-size: 18px; line-height: 25.5px; font-weight: 500;
  }
  .license__title { font-weight: 600; }
</style>
</head>
<body>
<div class="banner">
  <svg class="banner__shapes" width="720" height="1200" viewBox="0 0 720 1200">
    <defs>
      <linearGradient id="roofer-tones" x1="0" y1="0" x2="1" y2="1">
        <stop offset="0" stop-color="#c9dff0"/>
        <stop offset=".5" stop-color="#e69a3c"/>
        <stop offset="1" stop-color="#3a5fb0"/>
      </linearGradient>
      <linearGradient id="metal-roof-tones" x1="0" y1="0" x2="1" y2="1">
        <stop offset="0" stop-color="#dbe8f6"/>
        <stop offset=".6" stop-color="#7f9fc8"/>
        <stop offset="1" stop-color="#34405e"/>
      </linearGradient>
      <linearGradient id="timber-roof-tones" x1="0" y1="1" x2="1" y2="0">
        <stop offset="0" stop-color="#b98a52"/>
        <stop offset=".5" stop-color="#e8d3b6"/>
        <stop offset="1" stop-color="#7fb4ea"/>
      </linearGradient>
    </defs>
    <polygon class="band-blue" points="0,0 720,0 720,144 386,234 386,1200 0,1200" fill="var(--brand-blue)"/>
    <polygon role="img" aria-label="Photo: roofer in hard hat and overalls hammering on a timber roof" points="0,327 386,234 386,489 0,582" fill="url(#roofer-tones)"/>
    <polygon role="img" aria-label="Photo: worker in safety vest fastening a corrugated metal roof" points="0,582 386,489 386,717 0,813" fill="url(#metal-roof-tones)"/>
    <polygon role="img" aria-label="Photo: roofer swinging a hammer on a sloped timber roof frame" points="0,813 386,717 386,975 0,1086" fill="url(#timber-roof-tones)"/>
  </svg>

  <header class="brand">
    <div class="brand__name">CRESTLINE</div>
    <div class="brand__tagline">ROOFING &amp; WATERPROOFING</div>
  </header>

  <h1 class="headline">WE ARE EXPERT<br>IN ROOFING &amp;<br>WATERPROOFING</h1>

  <section class="services">
    <h2 class="services__title">OUR SERVICES</h2>
    <div class="service-group">
      <h3 class="service-group__title">HOA &amp; COMMERCIAL ROOFING</h3>
      <ul class="service-group__list">
        <li>Emergency Roof Tarping &amp; Repairs —<br>Starting at $550</li>
        <li>Small &amp; Large Roof Repairs</li>
        <li>Preventative Roof Maintenance</li>
        <li>Full Roof Replacement</li>
      </ul>
    </div>
    <div class="service-group">
      <h3 class="service-group__title">DECK &amp; BALCONY SERVICES</h3>
      <ul class="service-group__list">
        <li>Balcony &amp; Deck Maintenance<br>SB-326 Repairs</li>
        <li>Deck Resurfacing</li>
        <li>Small &amp; Large Deck Repairs</li>
        <li>Full Deck Reconstruction</li>
      </ul>
    </div>
    <div class="service-group">
      <h3 class="service-group__title">GUTTER SERVICES</h3>
      <ul class="service-group__list">
        <li>Small &amp; Large Gutter Repairs</li>
        <li>Gutter Cleaning &amp; Maintenance</li>
        <li>New Gutter Installation &amp;<br>Replacement</li>
      </ul>
    </div>
  </section>

  <section class="contact">
    <div class="contact__label">Contact Us:</div>
    <div class="contact__row">
      <svg class="contact__icon" viewBox="0 0 28 24" aria-hidden="true">
        <rect width="28" height="24" fill="var(--brand-blue)"/>
        <path d="M9 6c1-1 2-1 2.6 0l1.4 2.2c.4.7.2 1.3-.4 1.8l-.9.7c.8 1.8 2.1 3.2 3.9 4l.8-.9c.5-.6 1.2-.7 1.8-.3l2.1 1.4c.8.6.8 1.6 0 2.5-1.3 1.4-3 1.5-5.2.4C11.7 16.6 9 13.8 8 10.6c-.5-1.8 0-3.5 1-4.6z" fill="#f5c518"/>
      </svg>
      <div class="contact__phone">1-800-2731</div>
    </div>
    <div class="contact__label">Office Location:</div>
    <div class="contact__row">
      <svg class="contact__icon" viewBox="0 0 28 24" aria-hidden="true">
        <rect width="28" height="24" fill="var(--brand-blue)"/>
        <path d="M14 4a5.5 5.5 0 0 0-5.5 5.5C8.5 13.6 14 20 14 20s5.5-6.4 5.5-10.5A5.5 5.5 0 0 0 14 4zm0 7.6a2.1 2.1 0 1 1 0-4.2 2.1 2.1 0 0 1 0 4.2z" fill="#f5c518"/>
      </svg>
      <div class="contact__address">41 Dunwick Street, Suite F<br>Serving Orange County<br>&amp; Surrounding Areas</div>
    </div>
  </section>

  <section class="license">
    <div class="license__title">LICENSE INFORMATION:</div>
    <div>C-39 Roofing Contractor</div>
    <div>General B Contractor</div>
    <div>License #4529730</div>
  </section>
</div>
</body>
</html>
```